Unique Concept Design to Website Needed

Please see the attached folder. I have random images,etc but most importantly I have an attached image I was working on as a concept of a website. The brown background with blue and brown squares. logo in upper left and a little about me and then the squares would have names on them to lead to a section of the website with more info. I envision, when you mouse over a square, an image would appear so I attached random images here as well. Maybe some squares already have some images too.
- I want simple fonts. i like CLEAN, fonts
- text should be minimal. i am changing my site to less text, more powerful, bolder, larger lines with less content
- i am not sold on brown as the secondary color. i like blue but maybe grays, whites, offwhite scales or some other colors
-i have another graphic in there too
-you can see from my mock what company i am. please feel free to look me up and pull any portfolio , info , etc content to help make a great mock.
Do something cool!

```html
<!DOCTYPE html>
<html lang="en">
<head>
<meta charset="utf-8">
<title>Company Name — Profile</title>
<link rel="stylesheet" href="https://fonts.googleapis.com/css2?family=Ubuntu:wght@300;400;500;700&family=Nunito+Sans:wght@300;400;600&display=swap">
<style>
  :root {
    --bg-light: #e9f1f5;
    --bg-edge: #a9c8d7;
    --navy: #05527f;
    --slate: #3d6880;
    --sky: #06abf5;
    --white: #ffffff;
    --photo-warm: #b9a36c;
    --photo-dark: #5a4a32;
    --radius: 46px;
  }
  * { box-sizing: border-box; margin: 0; padding: 0; }
  html, body { width: 1200px; height: 960px; overflow: hidden; }
  body {
    position: relative;
    background: radial-gradient(ellipse 720px 640px at 560px 560px, var(--bg-light) 0%, #cfe0e9 55%, var(--bg-edge) 100%);
    font-family: "Ubuntu", sans-serif;
    color: var(--white);
  }

  .brand {
    position: absolute; left: 20px; top: 22px; width: 162px;
    display: flex; flex-direction: column; align-items: center;
  }
  .brand-mark {
    width: 120px; height: 120px; border-radius: 50%;
    border: 6px solid var(--white);
    margin-bottom: 28px;
  }
  .brand-name {
    font-family: "Ubuntu", sans-serif; font-weight: 700;
    font-size: 28px; line-height: 37px; text-align: center; letter-spacing: 0.2px;
  }

  .tile { position: absolute; overflow: hidden; }
  .tile-title { font-family: "Ubuntu", sans-serif; font-weight: 400; font-size: 27px; position: absolute; }

  .tile-about { left: 253px; top: 142px; width: 188px; height: 146px; background: var(--navy); border-top-left-radius: var(--radius); }
  .tile-back { left: 451px; top: 625px; width: 188px; height: 146px; background: var(--navy); border-bottom-left-radius: var(--radius); }
  .nav-label { width: 100%; text-align: center; top: 54px; font-weight: 300; font-size: 32px; }
  .corner { position: absolute; width: 35px; height: 35px; border-color: var(--white); border-style: solid; border-width: 0; }
  .corner-tr { border-top-width: 2px; border-right-width: 2px; }
  .corner-bl { border-bottom-width: 2px; border-left-width: 2px; }
  .corner-tl { border-top-width: 2px; border-left-width: 2px; }
  .corner-br { border-bottom-width: 2px; border-right-width: 2px; }

  .tile-skills { left: 451px; top: 142px; width: 386px; height: 146px; background: var(--slate); border-top-right-radius: var(--radius); }
  .tile-skills .tile-title { left: 10px; top: 6px; font-size: 26px; }
  .skills-chart { position: absolute; left: 0; top: 0; }
  .skill-label { font-family: "Nunito Sans", sans-serif; font-size: 16px; fill: var(--white); }

  .portrait { position: absolute; top: 297px; width: 188px; height: 316px; }
  .portrait-left { left: 253px; border-bottom-left-radius: var(--radius);
    background: linear-gradient(160deg, var(--photo-dark) 0%, #7e6a48 45%, #a6a67e 100%); }
  .portrait-right { left: 451px;
    background: linear-gradient(200deg, #e9e2a0 0%, var(--photo-warm) 45%, #8c8a6a 100%); }

  .tile-hobbies { left: 650px; top: 297px; width: 186px; height: 149px; background: var(--navy); }
  .tile-hobbies .tile-title { left: 14px; top: 8px; }

  .tile-contact { left: 846px; top: 297px; width: 188px; height: 149px; background: var(--sky); border-top-right-radius: var(--radius); }
  .tile-contact .tile-title { left: 17px; top: 8px; }
  .contact-list { list-style: none; }
  .contact-item { position: absolute; display: flex; align-items: center; font-family: "Nunito Sans", sans-serif; font-size: 18px; white-space: nowrap; }
  .contact-phone { left: 18px; top: 48px; }
  .contact-email { left: 14px; top: 109px; }
  .contact-phone svg { margin-right: 20px; }
  .contact-email svg { margin-right: 14px; }

  .tile-history { left: 650px; top: 456px; width: 384px; height: 315px; background: var(--slate); }
  .tile-history .tile-title { left: 16px; top: 24px; }
  .history-text {
    position: absolute; left: 16px; top: 73px; width: 360px;
    font-family: "Nunito Sans", sans-serif; font-weight: 300; font-size: 19px; line-height: 24.8px;
    white-space: nowrap;
  }
</style>
</head>
<body>
  <header class="brand">
    <div class="brand-mark"></div>
    <div class="brand-name">COMPANY<br>NAME</div>
  </header>

  <main>
    <a class="tile tile-about">
      <span class="corner corner-tr" style="right:5px; top:5px;"></span>
      <span class="corner corner-bl" style="left:5px; bottom:5px;"></span>
      <span class="tile-title nav-label">About</span>
    </a>

    <section class="tile tile-skills">
      <h2 class="tile-title">Skills</h2>
      <svg class="skills-chart" width="386" height="146" viewBox="0 0 386 146">
        <line x1="86" y1="17" x2="359" y2="17" stroke="#fff" stroke-width="2"/>
        <line x1="80" y1="116.5" x2="364" y2="116.5" stroke="#fff" stroke-width="1"/>
        <rect x="86" y="77" width="15" height="40" fill="#fff"/>
        <rect x="133" y="53" width="16" height="64" fill="#fff"/>
        <rect x="201" y="30" width="15" height="87" fill="#fff"/>
        <rect x="284" y="30" width="15" height="87" fill="#fff"/>
        <rect x="344" y="39" width="15" height="78" fill="#fff"/>
        <text class="skill-label" x="94" y="137" text-anchor="middle">Ps</text>
        <text class="skill-label" x="141" y="137" text-anchor="middle">Ai</text>
        <text class="skill-label" x="208" y="137" text-anchor="middle">HTML/CSS</text>
        <text class="skill-label" x="292" y="137" text-anchor="middle">JAVA</text>
        <text class="skill-label" x="352" y="137" text-anchor="middle">PHP</text>
      </svg>
    </section>

    <div class="portrait portrait-left" role="img" aria-label="Portrait photo of the site owner, left half"></div>
    <div class="portrait portrait-right" role="img" aria-label="Portrait photo of the site owner, right half"></div>

    <section class="tile tile-hobbies">
      <h2 class="tile-title">Hobbies</h2>
    </section>

    <section class="tile tile-contact">
      <h2 class="tile-title">Contact</h2>
      <ul class="contact-list">
        <li class="contact-item contact-phone">
          <svg width="26" height="40" viewBox="0 0 26 40" aria-hidden="true">
            <path d="M7 1 L11 1 L12 11 L8 13 C7 19 8 25 11 30 L15 28 L20 36 L16 39 C8 40 2 31 1 21 C0 11 3 3 7 1 Z" fill="#fff"/>
          </svg>
          <span>50 000 123</span>
        </li>
        <li class="contact-item contact-email">
          <svg width="37" height="23" viewBox="0 0 37 23" aria-hidden="true">
            <rect x="1" y="1" width="35" height="21" fill="none" stroke="#fff" stroke-width="2"/>
            <path d="M1 1 L18.5 14 L36 1 M1 22 L14 10 M36 22 L23 10" fill="none" stroke="#fff" stroke-width="2"/>
          </svg>
          <span>hi@mail.com</span>
        </li>
      </ul>
    </section>

    <section class="tile tile-history">
      <h2 class="tile-title">History</h2>
      <p class="history-text">"Lorem ipsum dolor sit amet,<br>consectetur adipisicing elit, sed do<br>eiusmod tempor incididunt ut labore et<br>dolore magna aliqua. Ut enim ad minim<br>veniam, quis nostrud exercitation<br>ullamco laboris nisi ut aliquip ex ea<br>commodo consequat. Duis aute irure<br>dolor in reprehenderit in voluptate velit<br>esse cillum dolore eu fugiat nulla</p>
    </section>

    <a class="tile tile-back">
      <span class="corner corner-tl" style="left:5px; top:6px;"></span>
      <span class="corner corner-br" style="right:5px; bottom:5px;"></span>
      <span class="tile-title nav-label">Back</span>
    </a>
  </main>
</body>
</html>
```